ORVA TELMINO - LUXURY RESORT CORVANE HOTEL

We wanna promote the luxury hotel based on marroquian stylish luxury decor, it is still a project but we need to expose it.
Houses will be A frame type houses surrounded by florest and water dumps - please check - odeleite amber heron at google to check localisation
Container luxury houses also will be included heaven blue velvet and green and rose gold are the Color. The sky is the limit.

```html
<!DOCTYPE html>
<html lang="en">
<head>
<meta charset="utf-8">
<title>Orva Telmino – Business Card</title>
<link rel="stylesheet" href="https://fonts.googleapis.com/css2?family=Cinzel:wght@400;500&family=Arimo:wght@400;700&display=swap">
<style>
  :root {
    --stage: #1f2729;
    --gold: #c89d6d;
    --title-gold: #e3c35a;
    --card-light: #f2f2f2;
    --card-dark: #2a2525;
    --forest: #10281d;
    --ink: #2a2a2a;
    --ink-soft: #3a3a3a;
    --tagline: #ece6df;
  }
  * { margin: 0; padding: 0; box-sizing: border-box; }
  html, body { width: 1200px; height: 925px; overflow: hidden; background: var(--stage); }
  .canvas { position: relative; width: 1200px; height: 925px; background: var(--stage); }

  .sheet-title {
    position: absolute; top: 52px; right: 80px;
    font-family: "Cinzel", serif; font-size: 19px; letter-spacing: 2px;
    color: var(--title-gold); font-variant: small-caps;
  }

  .card {
    position: absolute; top: 320px; width: 530px; height: 304px;
    border-radius: 16px; overflow: hidden;
  }

  /* Front */
  .card-front { left: 45px; background: var(--card-light); }
  .front-photo {
    position: absolute; top: 0; right: 0; width: 190px; height: 100%;
    background: linear-gradient(180deg, #d9d9d9 0%, #8a8784 35%, #3d3a37 60%, #5a554f 100%);
    border-left: 5px solid var(--forest);
  }
  .front-identity { position: absolute; left: 36px; top: 62px; font-family: "Arimo", sans-serif; }
  .person-name { font-size: 26px; font-weight: 400; color: var(--ink-soft); letter-spacing: .2px; }
  .person-role { font-size: 15px; font-weight: 700; color: #111; margin-top: 1px; }
  .front-rule { position: absolute; left: 0; top: 150px; width: 245px; height: 7px; background: var(--forest); }
  .front-rule-thin { position: absolute; left: 245px; top: 150px; width: 95px; height: 2px; background: var(--forest); }

  .contact-list { position: absolute; left: 36px; top: 172px; list-style: none; font-family: "Arimo", sans-serif; }
  .contact-item { display: flex; align-items: center; gap: 10px; height: 20px; font-size: 11.5px; color: var(--ink); }
  .contact-item:first-child { font-weight: 700; }
  .contact-icon { width: 15px; height: 15px; flex: none; }

  .front-brand {
    position: absolute; left: 120px; bottom: 24px;
    font-family: "Cinzel", serif; font-size: 22px; letter-spacing: 3px; color: var(--ink);
  }

  /* Back */
  .card-back { left: 625px; background: var(--card-dark); }
  .back-tick { position: absolute; left: 50%; width: 4px; height: 24px; margin-left: -2px; background: var(--gold); }
  .back-tick.top { top: 0; }
  .back-tick.bottom { bottom: 0; }
  .back-brand {
    position: absolute; top: 104px; width: 100%; text-align: center;
    font-family: "Cinzel", serif; font-size: 34px; letter-spacing: 5px; color: var(--gold);
  }
  .back-tagline {
    position: absolute; top: 164px; width: 100%; text-align: center;
    font-family: "Cinzel", serif; font-size: 15px; letter-spacing: 3px; color: var(--tagline);
  }
</style>
</head>
<body>
<main class="canvas">
  <h1 class="sheet-title">Business Card- mock up 1</h1>

  <section class="card card-front" aria-label="Business card front">
    <div class="front-identity">
      <p class="person-name">Nadia Kessoury</p>
      <p class="person-role">Founder &amp; Head of Design</p>
    </div>
    <div class="front-rule"></div>
    <div class="front-rule-thin"></div>

    <ul class="contact-list">
      <li class="contact-item">
        <svg class="contact-icon" viewBox="0 0 16 16"><circle cx="8" cy="8" r="8" fill="#10281d"/><path d="M5.3 4.2l1.3 1.6-.7 1c.5 1 1.2 1.7 2.2 2.2l1-.7 1.6 1.3-.8 1.2C7.4 10.6 5.4 8.6 4.2 6z" fill="#fff"/></svg>
        +20 1X XXXX XXXX
      </li>
      <li class="contact-item">
        <svg class="contact-icon" viewBox="0 0 16 16"><circle cx="8" cy="8" r="8" fill="#10281d"/><circle cx="8" cy="8" r="4" fill="none" stroke="#fff" stroke-width=".9"/><path d="M4 8h8M8 4c-1.5 2.4-1.5 5.6 0 8M8 4c1.5 2.4 1.5 5.6 0 8" fill="none" stroke="#fff" stroke-width=".8"/></svg>
        www.velmorastudio.com
      </li>
      <li class="contact-item">
        <svg class="contact-icon" viewBox="0 0 16 16"><circle cx="8" cy="8" r="8" fill="#10281d"/><rect x="4" y="5.2" width="8" height="5.6" fill="none" stroke="#fff" stroke-width=".9"/><path d="M4 5.2l4 3 4-3" fill="none" stroke="#fff" stroke-width=".9"/></svg>
        Nadia.Kessoury@velmorastudio.com
      </li>
      <li class="contact-item">
        <svg class="contact-icon" viewBox="0 0 16 16"><circle cx="8" cy="8" r="8" fill="#10281d"/><path d="M8 12.5S5 9.3 5 7a3 3 0 016 0c0 2.3-3 5.5-3 5.5z" fill="#fff"/><circle cx="8" cy="7" r="1.1" fill="#10281d"/></svg>
        Miraval St – Sendra, Cairo, Egypt
      </li>
    </ul>

    <p class="front-brand">ORVA TELMINO</p>

    <div class="front-photo" role="img" aria-label="Photo of a black A-frame tiny house suspended over a rocky cliff, captioned 'Suspended tiny house in California'"></div>
  </section>

  <section class="card card-back" aria-label="Business card back">
    <span class="back-tick top"></span>
    <p class="back-brand">ORVA TELMINO</p>
    <p class="back-tagline">Luxury Resort Corvane Hotel</p>
    <span class="back-tick bottom"></span>
  </section>
</main>
</body>
</html>
```